Kivora - a fintech company - business card

We need a business card design for our Payments Technology company in Sydney, Australia. We provide business with payment solutions expanding across EFTPOS machines, online payment gateways and mobile payment solutions. We would like to see designs that are clean, classy and professional.
Target Market(s)
Business professionals, executives, c-suite
Industry/Entity Type
Fintech
Contact Information for Business Card
Will be on 400gsm. Logo will most likely be spot gloss unless designer recommends otherwise.
Font styles to use
Sans Serif
Requirements
Must have
- We need our website (kivora.com.au), email (contact@kivora.com.au), mobile (0455 806 274) and direct phone number (02 7391 5082) to feature on the card along with our logo (attached) and the words "EFTPOS | ONLINE | MOBILE"
- Font = Roboto

```html
<!DOCTYPE html>
<html lang="en">
<head>
<meta charset="utf-8">
<title>Kivora – Business Card</title>
<link rel="stylesheet" href="https://fonts.googleapis.com/css2?family=Roboto:wght@400;500;700;900&family=Open+Sans:wght@400;600&display=swap">
<style>
  :root {
    --stage: #2b2b2d;
    --brand-blue: #2a679d;
    --brand-blue-light: #3a7bb3;
    --brand-grey: #5d5e62;
    --swoosh-grey: #6f7074;
    --text-grey: #616166;
    --paper: #ffffff;
  }
  * { margin: 0; padding: 0; box-sizing: border-box; }
  html, body {
    width: 1200px; height: 900px; overflow: hidden;
    background: var(--stage);
  }
  .stage {
    position: relative; width: 1200px; height: 900px;
  }
  .card {
    position: absolute; left: 290px; width: 620px; height: 354px;
    overflow: hidden; box-shadow: 0 12px 30px rgba(0,0,0,.45);
  }

  /* Front */
  .card--front {
    top: 70px;
    background: radial-gradient(ellipse at 55% 45%, var(--brand-blue-light) 0%, var(--brand-blue) 65%);
    color: var(--paper);
    display: flex; flex-direction: column; align-items: center; justify-content: center;
  }
  .front__wordmark {
    font-family: "Roboto", sans-serif; font-weight: 900;
    font-size: 64px; letter-spacing: 1px; line-height: 1;
  }
  .front__services {
    margin-top: 34px;
    font-family: "Open Sans", sans-serif; font-weight: 400;
    font-size: 19px; letter-spacing: 1.5px;
  }

  /* Back */
  .card--back {
    top: 470px; background: var(--paper);
  }
  .back__wave { position: absolute; left: 0; top: 0; width: 620px; height: 354px; }
  .back__brand {
    position: absolute; left: 34px; top: 62px; width: 240px;
    display: flex; flex-direction: column; align-items: center;
  }
  .brand__dot {
    width: 86px; height: 86px; border-radius: 50%; background: var(--brand-blue);
  }
  .brand__name {
    margin-top: 14px;
    font-family: "Roboto", sans-serif; font-weight: 900;
    font-size: 50px; color: var(--brand-grey); line-height: 1;
  }
  .back__divider {
    position: absolute; left: 296px; top: 62px; width: 2px; height: 170px;
    background: var(--swoosh-grey);
  }
  .back__details {
    position: absolute; left: 318px; top: 66px;
    font-family: "Open Sans", sans-serif; color: var(--text-grey);
  }
  .details__name {
    font-family: "Roboto", sans-serif; font-weight: 700;
    font-size: 22px; color: var(--brand-blue); line-height: 1.1;
  }
  .details__title { font-size: 17px; line-height: 1.3; }
  .contact-list { list-style: none; margin-top: 12px; }
  .contact-list li {
    display: flex; align-items: center; gap: 10px;
    font-size: 15px; line-height: 22px;
  }
  .contact-list svg { width: 16px; height: 16px; fill: var(--brand-blue); flex: none; }
</style>
</head>
<body>
<main class="stage">

  <section class="card card--front">
    <div class="front__wordmark">KIVORA</div>
    <div class="front__services">EFTPOS | ONLINE | MOBILE</div>
  </section>

  <section class="card card--back">
    <svg class="back__wave" viewBox="0 0 620 354" aria-hidden="true">
      <path d="M0,196 C70,250 150,272 320,276 C200,272 90,250 0,212 Z" fill="var(--swoosh-grey)"/>
      <path d="M0,222 C60,262 150,286 300,290 C440,294 540,282 620,268 L620,354 L0,354 Z" fill="var(--brand-blue)"/>
    </svg>

    <div class="back__brand">
      <div class="brand__dot"></div>
      <div class="brand__name">KIVORA</div>
    </div>

    <div class="back__divider"></div>

    <div class="back__details">
      <div class="details__name">YOUR NAME</div>
      <div class="details__title">Your Title</div>
      <ul class="contact-list">
        <li>
          <svg viewBox="0 0 24 24"><path d="M6.6 10.8a15.1 15.1 0 0 0 6.6 6.6l2.2-2.2c.3-.3.7-.4 1-.2 1.1.4 2.3.6 3.6.6.6 0 1 .4 1 1V20c0 .6-.4 1-1 1A17 17 0 0 1 3 4c0-.6.4-1 1-1h3.5c.6 0 1 .4 1 1 0 1.3.2 2.5.6 3.6.1.3 0 .7-.2 1z"/></svg>
          0455 806 274
        </li>
        <li>
          <svg viewBox="0 0 24 24"><path d="M7 1h10a2 2 0 0 1 2 2v18a2 2 0 0 1-2 2H7a2 2 0 0 1-2-2V3a2 2 0 0 1 2-2zm0 3v14h10V4zm5 15.5a1 1 0 1 0 0 2 1 1 0 0 0 0-2z"/></svg>
          02 7391 5082
        </li>
        <li>
          <svg viewBox="0 0 24 24"><path d="M2 5h20v14H2zm2 2v.5l8 5 8-5V7zm0 2.8V17h16V9.8l-8 5z"/></svg>
          contact@kivora.com.au
        </li>
        <li>
          <svg viewBox="0 0 24 24"><path d="M12 2a10 10 0 1 0 0 20 10 10 0 0 0 0-20zm0 2c1 0 2.3 2 2.8 5H9.2C9.7 6 11 4 12 4zM4.3 11h3.8c0 .7 0 1.3.1 2H4.3a8 8 0 0 1 0-2zm5.8 0h3.8v2h-3.8zm5.8 0h3.8a8 8 0 0 1 0 2h-3.8zM9.2 15h5.6c-.5 3-1.8 5-2.8 5s-2.3-2-2.8-5z"/></svg>
          kivora.com.au
        </li>
      </ul>
    </div>
  </section>

</main>
</body>
</html>
```